Local fast-growing company in the service sector

We are looking for a modern business card design, which should also appear on our letterheads

Target Market(s)

Private and industrial sectors

Contact Information for Business Card

Vorname Name
Lindkofer Str. 18
71468 Remsbach
Tel.: 07163-418259-0
Name@kovaltec-pbz.de

Colors
9d9d9d
919191
aaaaaa

Requirements
Must have
• The logo (file) in silver

```html
<!DOCTYPE html>
<html lang="de">
<head>
<meta charset="utf-8">
<title>PBZ – Visitenkarte</title>
<link rel="stylesheet" href="https://fonts.googleapis.com/css2?family=Poppins:wght@400;500;700&family=Open+Sans:wght@400&display=swap">
<style>
  :root {
    --stage: #e8e5e0;
    --card-white: #ffffff;
    --silver-light: #d6d6d6;
    --silver: #aaaaaa;
    --silver-mid: #9d9d9d;
    --silver-dark: #919191;
    --band-dark: #3b3b3b;
    --card-black: #050505;
    --ink: #111111;
    --paper-text: #f2f2f2;
  }
  * { margin: 0; padding: 0; box-sizing: border-box; }
  html, body { width: 1200px; height: 831px; overflow: hidden; }
  body { background: var(--stage); position: relative; }

  .business-card {
    position: absolute;
    left: 100px; top: 132px;
    width: 1000px; height: 568px;
    background: var(--card-white);
    overflow: hidden;
    box-shadow: 0 6px 18px rgba(0,0,0,0.18);
  }
  .card-shapes { position: absolute; inset: 0; width: 100%; height: 100%; }

  .brand {
    position: absolute; left: 44px; top: 50px;
    display: flex; align-items: center; gap: 16px;
  }
  .brand-square { width: 64px; height: 64px; background: var(--silver-mid); }
  .brand-name {
    font-family: "Poppins", sans-serif; font-weight: 700;
    font-size: 70px; line-height: 1; color: var(--silver-dark);
    letter-spacing: 1px;
  }

  .holder { position: absolute; right: 42px; top: 236px; text-align: right; color: var(--ink); }
  .holder-name {
    font-family: "Poppins", sans-serif; font-weight: 400;
    font-size: 52px; line-height: 1;
  }
  .holder-role {
    font-family: "Poppins", sans-serif; font-weight: 500;
    font-size: 20px; line-height: 1; letter-spacing: 4px; margin-top: 8px; margin-right: -4px;
  }

  .contact {
    position: absolute; color: var(--paper-text);
    font-family: "Open Sans", sans-serif; font-size: 24px; line-height: 1;
    display: flex; align-items: center; gap: 14px;
  }
  .contact svg { fill: var(--paper-text); flex: none; }
  .contact-address { left: 22px; top: 450px; }
  .contact-phone { right: 38px; top: 450px; }
  .contact-mail { right: 38px; top: 486px; }
</style>
</head>
<body>
  <div class="business-card">
    <svg class="card-shapes" viewBox="0 0 1000 568" preserveAspectRatio="none" aria-hidden="true">
      <defs>
        <linearGradient id="silverSweep" x1="0" y1="0" x2="1" y2="0">
          <stop offset="0" stop-color="var(--silver-dark)"/>
          <stop offset="0.55" stop-color="var(--silver)"/>
          <stop offset="1" stop-color="var(--silver-light)"/>
        </linearGradient>
        <linearGradient id="lineSweep" x1="0" y1="0" x2="1" y2="0">
          <stop offset="0" stop-color="#6f6f6f"/>
          <stop offset="1" stop-color="var(--silver)"/>
        </linearGradient>
      </defs>
      <polygon class="silver-stripe" points="0,276 1000,2 1000,10 0,288" fill="url(#lineSweep)"/>
      <polygon class="silver-field" points="0,302 1000,20 1000,345 0,345" fill="url(#silverSweep)"/>
      <polygon class="dark-band" points="0,332 1000,334 1000,366 0,380" fill="var(--band-dark)"/>
      <polygon class="black-field" points="0,374 1000,358 1000,568 0,568" fill="var(--card-black)"/>
      <rect class="white-rule" x="0" y="498" width="628" height="5" fill="#d9d9d9"/>
    </svg>

    <div class="brand">
      <span class="brand-square"></span>
      <span class="brand-name">PBZ</span>
    </div>

    <div class="holder">
      <div class="holder-name">Jonas Berger</div>
      <div class="holder-role">DIRECTOR</div>
    </div>

    <div class="contact contact-address">
      <svg width="18" height="24" viewBox="0 0 18 24"><path d="M9 0C4 0 0 4 0 9c0 6.5 9 15 9 15s9-8.5 9-15c0-5-4-9-9-9zm0 12.5A3.5 3.5 0 1 1 9 5.5a3.5 3.5 0 0 1 0 7z"/></svg>
      <span>Lindkofer Str. 18, 71468 Remsbach</span>
    </div>

    <div class="contact contact-phone">
      <span>07163-418259-0</span>
      <svg width="22" height="22" viewBox="0 0 24 24"><path d="M6.6 10.8a15.1 15.1 0 0 0 6.6 6.6l2.2-2.2c.3-.3.7-.4 1-.2 1.1.4 2.3.6 3.6.6.6 0 1 .4 1 1V20c0 .6-.4 1-1 1A17 17 0 0 1 3 4c0-.6.4-1 1-1h3.5c.6 0 1 .4 1 1 0 1.3.2 2.5.6 3.6.1.3 0 .7-.2 1z"/></svg>
    </div>

    <div class="contact contact-mail">
      <span>Name@kovaltec-pbz.de</span>
      <svg width="22" height="16" viewBox="0 0 22 16"><path d="M0 0h22v16H0zM1.5 1.5 11 9l9.5-7.5z" fill-rule="evenodd"/></svg>
    </div>
  </div>
</body>
</html>
```